FB and Youtube banner design for HVAC company

I would like an appealing site page banner for business page on Facebook (851w x 315h pixels) and one for youtube (2560w x 1440h pixels) for hvac company. Business card design and logo are attached. Company name is Bright Meadow Air Conditioning, Refrigeration, and Heating.

NOTE: I put the business cards and log up to see some of the artwork the company is using. It's not to replicate that in the banner images.

Target Market(s)

Interested business and homeowner visitors to Facebook business page and youtube channel page.

Industry/Entity Type

Hvac

Font styles to use
Sans Serif

Requirements
Must have
• See logo for color scheme.
Should not have
• This should not look like a business card. Think of what is typically the banner on a facebook business page and youtube channel.

```html
<!DOCTYPE html>
<html lang="en">
<head>
<meta charset="utf-8">
<title>Bright Meadow – Social Banners</title>
<link rel="stylesheet" href="https://fonts.googleapis.com/css2?family=Archivo+Black&family=Michroma&display=swap">
<style>
  :root {
    --page: #ffffff;
    --navy: #2b3990;
    --navy-deep: #263385;
    --sky: #1ea6e6;
    --ember: #f26a22;
    --white: #ffffff;
  }
  * { margin: 0; padding: 0; box-sizing: border-box; }
  html, body {
    width: 1200px;
    height: 1200px;
    overflow: hidden;
    background: var(--page);
  }
  .canvas {
    position: relative;
    width: 1200px;
    height: 1200px;
    background: var(--page);
  }
  .banner {
    position: absolute;
    overflow: hidden;
  }
  .banner--facebook { left: 103px; top: 126px; width: 1011px; height: 375px; }
  .banner--youtube  { left: 154px; top: 609px; width: 886px;  height: 497px; }

  .banner__pattern {
    position: absolute;
    inset: 0;
    background:
      radial-gradient(circle at 10% 25%, rgba(242,106,34,0.35), transparent 22%),
      radial-gradient(circle at 90% 40%, rgba(30,166,230,0.40), transparent 25%),
      radial-gradient(circle at 8% 90%, rgba(30,166,230,0.35), transparent 22%),
      radial-gradient(circle at 55% 95%, rgba(242,106,34,0.25), transparent 18%),
      radial-gradient(circle at 45% 5%, rgba(242,106,34,0.25), transparent 18%),
      linear-gradient(135deg, var(--navy), var(--navy-deep));
  }

  .brand {
    position: absolute;
    display: flex;
    align-items: center;
    gap: 26px;
  }
  .brand__mark {
    flex: none;
    width: 150px;
    height: 150px;
    border-radius: 50%;
    background: var(--ember);
  }
  .brand__name {
    font-family: "Archivo Black", "Arial Black", sans-serif;
    font-size: 76px;
    line-height: 0.98;
    color: var(--white);
    text-transform: uppercase;
    letter-spacing: -1px;
  }

  .tagline {
    position: absolute;
    font-family: "Michroma", sans-serif;
    font-size: 14.5px;
    color: var(--white);
    letter-spacing: 1.6px;
    white-space: nowrap;
    text-transform: uppercase;
  }

  .banner--facebook .brand   { left: 240px; top: 96px; }
  .banner--facebook .tagline { left: 240px; top: 278px; }

  .banner--youtube .brand    { left: 158px; top: 172px; }
  .banner--youtube .tagline  { left: 155px; top: 352px; }
</style>
</head>
<body>
<main class="canvas">

  <section class="banner banner--facebook" aria-label="Facebook page banner">
    <div class="banner__pattern" role="img" aria-label="Scattered orange and light blue snowflake pattern on a navy background"></div>
    <div class="brand">
      <span class="brand__mark" aria-hidden="true"></span>
      <h1 class="brand__name">Bright<br>Meadow</h1>
    </div>
    <p class="tagline">Air Conditioning - Refrigeration - Heating</p>
  </section>

  <section class="banner banner--youtube" aria-label="YouTube channel banner">
    <div class="banner__pattern" role="img" aria-label="Scattered orange and light blue snowflake pattern on a navy background"></div>
    <div class="brand">
      <span class="brand__mark" aria-hidden="true"></span>
      <h2 class="brand__name">Bright<br>Meadow</h2>
    </div>
    <p class="tagline">Air Conditioning - Refrigeration - Heating</p>
  </section>

</main>
</body>
</html>
```